Apricot Variety Sheet - Meadowlark Orchard Co

We are needing a variety sheet that we can hand out that will describe the different apricot vatieties we have available. The attached document has the name of the variety along with a description that will need to be on the sheet. We are looking for a modern, appealing way to display this information on 1 page (if needed, it can be front and back)
Updates

Apologies for the delay; we are overwhelmed with the great design options and will be sorting through them all (across our contests) to pick a collective. Thank you for your patience.

Target Market(s)

Growers and consumers

Industry/Entity Type

Agriculture

Requirements
Must have
• Easy to read
• Natural color palettes to emphasize the agricultural nature
• Clearly show washington as the origin in the title or at the top
Nice to have
• incorporate Apricots in the design

```html
<!DOCTYPE html>
<html lang="en">
<head>
<meta charset="utf-8">
<title>Apricot Varieties – Meadowlark Orchard Co, Washington State</title>
<link href="https://fonts.googleapis.com/css2?family=Lato:wght@400;700;900&display=swap" rel="stylesheet">
<style>
  :root {
    --sun-light: #fde7a6;
    --sun-mid: #fccf5e;
    --sun-deep: #f8b52a;
    --apricot: #f39a1f;
    --apricot-deep: #e0651c;
    --leaf: #1c7a4b;
    --ink: #1b1b1b;
  }
  * { margin: 0; padding: 0; box-sizing: border-box; }
  html, body { width: 849px; height: 1200px; overflow: hidden; }
  body {
    font-family: "Lato", Arial, sans-serif;
    color: var(--ink);
    background: var(--sun-mid);
  }
  .sheet {
    position: relative;
    width: 849px;
    height: 1200px;
    overflow: hidden;
    background:
      radial-gradient(ellipse 70% 45% at 35% 18%, var(--sun-light) 0%, rgba(253,231,166,0) 100%),
      linear-gradient(180deg, #fde39a 0%, var(--sun-mid) 40%, var(--sun-deep) 70%, var(--apricot) 100%);
  }
  .fruit-photo {
    position: absolute;
    left: 0; right: 0; bottom: 0;
    height: 520px;
    background:
      radial-gradient(ellipse 28% 32% at 63% 78%, #f7b94a 0%, #f5a132 55%, rgba(245,161,50,0) 100%),
      radial-gradient(ellipse 25% 30% at 12% 85%, #f8c54c 0%, #f2a431 60%, rgba(242,164,49,0) 100%),
      radial-gradient(ellipse 22% 22% at 38% 40%, #fbd37a 0%, rgba(251,211,122,0) 100%),
      radial-gradient(ellipse 20% 30% at 95% 70%, #e8742c 0%, rgba(232,116,44,0) 100%),
      linear-gradient(180deg, rgba(248,181,42,0) 0%, #f4a230 30%, #ea8a28 70%, #e07a25 100%);
  }
  .masthead {
    position: absolute;
    top: 22px; left: 160px;
    display: flex;
    align-items: center;
    gap: 22px;
  }
  .masthead-mark {
    width: 138px; height: 128px;
    border-radius: 50%;
    background: var(--apricot-deep);
    flex: none;
  }
  .masthead-name {
    font-weight: 900;
    font-size: 38px;
    line-height: 38px;
    color: var(--leaf);
    margin-top: 8px;
  }
  .variety {
    position: absolute;
    width: 348px;
    font-size: 16.4px;
    line-height: 20.6px;
    text-align: justify;
    hyphens: auto;
    -webkit-hyphens: auto;
  }
  .variety-name { font-weight: 900; }
  .col-left { left: 56px; }
  .col-right { left: 444px; }
</style>
</head>
<body>
<main class="sheet">
  <div class="fruit-photo" role="img" aria-label="Photograph of whole and halved ripe apricots with a green leaf"></div>

  <header class="masthead">
    <div class="masthead-mark"></div>
    <h1 class="masthead-name">Meadowlark Orchard Co<br>Washington State</h1>
  </header>

  <p class="variety col-left" style="top:166px"><span class="variety-name">RIVAL –</span> Great flavor with a fine, firm texture distinguishes this large oval-shaped apricot. The skin is light orange with a red blush. The flesh is a lush deep orange color. Available early July- early August.</p>
  <p class="variety col-left" style="top:283px"><span class="variety-name">PERFECTION –</span> This classic large oval apricot is deep orange with an oblong shape and firm texture. The flesh is a yellow/orange color that is very sweet and full of flavor. Available mid July - mid August.</p>
  <p class="variety col-left" style="top:401px"><span class="variety-name">TOMCOT –</span> Tangy, sweet flavor with a firm texture. This oval apricot is light orange with a slight blush color. The flesh is a dark orange. Available late June – late July.</p>
  <p class="variety col-left" style="top:503px"><span class="variety-name">CASSELBRITE –</span> This medium sized apricot is golden orange with a slight red blush. It has a mild sweet-tart flavor that is good for eating out of hand. Available late June- early July.</p>
  <p class="variety col-left" style="top:617px"><span class="variety-name">SWEET JUILLET –</span> This special variety has a unique, sweet flavor with a juicy flesh. It is bright orange in color with a bright orange flesh. Available through July.</p>
  <p class="variety col-left" style="top:718px"><span class="variety-name">GOLDSTRIKE –</span> A larger apricot with light orange, blushed skin. Firm texture with a slight tart taste until fully ripened, then very sweet. Available mid June - mid July.</p>

  <p class="variety col-right" style="top:166px"><span class="variety-name">ROBADA –</span> This jumbo apricot has a delicious floral flavor with a firm texture. Bright orange, with a deep red blush over nearly half its surface. Available early June.</p>
  <p class="variety col-right" style="top:281px"><span class="variety-name">PATTERSON –</span> This apricot has a well-balanced flavor and an excellent shelf life. This is perfect for canning or drying. It has streaked red over yellow skin, with a firm flesh. Available mid – late June.</p>
  <p class="variety col-right" style="top:401px"><span class="variety-name">GOLDRICH –</span> This apricot is round with a bright orange skin color and a deep orange flesh. It has a mild, sweet flavor with a firm texture. Available early July – mid August.</p>
  <p class="variety col-right" style="top:502px"><span class="variety-name">GOLDBAR –</span> Moderately juicy, this large oval-shaped apricot has a light yellow-orange with a reddish blush. The flesh is firm, meaty, and has a light orange color. Available late June – end of July.</p>
  <p class="variety col-right" style="top:617px"><span class="variety-name">TASTY RICH –</span> This early variety is light yellow-orange colored with a firm texture. Very juicy with an enticing flavor. Available through June.</p>
  <p class="variety col-right" style="top:718px"><span class="variety-name">RILAND –</span> Very aromatic and sweet, this apricot is orange with a red blush. It has a yellow-orange colored flesh and a round shape. Available mid-June to end of July.</p>
</main>
</body>
</html>
```